Company or website name
- Marla Quist Design & Decor
- Passionate about wedding floral design and decor. Events I create are timeless, classic and elegant, customized 100% to the brides’ desires. Inspiring them with a vision of what is possible & asking them to step inside it and see it for themselves

```html
<!DOCTYPE html>
<html lang="en">
<head>
<meta charset="utf-8">
<title>Marla Quist Design &amp; Decor — Stationery</title>
<link rel="stylesheet" href="https://fonts.googleapis.com/css2?family=Cormorant+Garamond:wght@400;500&family=Lato:wght@300&display=swap">
<style>
  :root {
    --coral: #f06e6e;
    --blush: #f3a59c;
    --paper: #ffffff;
    --backdrop: #ffffff;
    --shadow: rgba(0, 0, 0, 0.45);
  }
  * { margin: 0; padding: 0; box-sizing: border-box; }
  html, body {
    width: 1082px;
    height: 1200px;
    overflow: hidden;
    background: var(--backdrop);
  }
  body {
    position: relative;
    font-family: "Lato", "Gill Sans", sans-serif;
    font-weight: 300;
    color: var(--coral);
  }
  .sheet {
    position: absolute;
    background: var(--paper);
    box-shadow: 3px 4px 6px var(--shadow);
  }
  .wordmark {
    position: absolute;
    font-family: "Cormorant Garamond", Garamond, serif;
    font-weight: 500;
    color: var(--coral);
    line-height: 1;
    white-space: nowrap;
  }
  .tagline {
    position: absolute;
    font-family: "Cormorant Garamond", Garamond, serif;
    font-weight: 400;
    color: var(--blush);
    line-height: 1;
    white-space: nowrap;
  }

  /* Letterhead */
  .letterhead {
    left: 188px;
    top: 52px;
    width: 860px;
    height: 1116px;
  }
  .letterhead__contact {
    position: absolute;
    right: 22px;
    top: 50px;
    height: 792px;
    writing-mode: vertical-rl;
    transform: rotate(180deg);
    font-size: 16.5px;
    letter-spacing: 0.4px;
    white-space: nowrap;
    text-align: left;
  }
  .letterhead__mark {
    position: absolute;
    left: 124px;
    top: 844px;
    width: 144px;
    height: 144px;
    border-radius: 50%;
    background: var(--coral);
  }
  .letterhead__name {
    left: 45px;
    top: 980px;
    font-size: 60px;
    letter-spacing: 0.5px;
  }
  .letterhead__tagline {
    left: 301px;
    top: 1040px;
    font-size: 29px;
  }

  /* Business card */
  .card {
    left: 41px;
    top: 155px;
    width: 210px;
    height: 359px;
    z-index: 2;
  }
  .card__details {
    position: absolute;
    right: 25px;
    top: 25px;
    text-align: right;
    font-size: 10px;
    line-height: 14px;
  }
  .card__person {
    font-size: 12.5px;
    margin-bottom: 14px;
  }
  .card__mark {
    position: absolute;
    left: 47px;
    top: 240px;
    width: 58px;
    height: 58px;
    border-radius: 50%;
    background: var(--coral);
  }
  .card__name {
    left: 13px;
    top: 300px;
    font-size: 25px;
  }
  .card__tagline {
    left: 96px;
    top: 326px;
    font-size: 14px;
  }
</style>
</head>
<body>
  <section class="sheet letterhead" aria-label="Letterhead">
    <p class="letterhead__contact">Marla Quist Design &amp; Decor . 123 Street Address . City, State 12345 . 222.555.1212 . address@email.com</p>
    <div class="letterhead__mark" aria-hidden="true"></div>
    <p class="wordmark letterhead__name">Marla Quist</p>
    <p class="tagline letterhead__tagline">design &amp; decor</p>
  </section>

  <section class="sheet card" aria-label="Business card">
    <div class="card__details">
      <p class="card__person">Marla Quist</p>
      <p>123 Street Address</p>
      <p>City, State 12345</p>
      <p>222.555.1212</p>
      <p>address@email.com</p>
    </div>
    <div class="card__mark" aria-hidden="true"></div>
    <p class="wordmark card__name">Marla Quist</p>
    <p class="tagline card__tagline">design &amp; decor</p>
  </section>
</body>
</html>
```